"Show Times" Poster for Stunt Show

I need a fairly simple 24"x 36" poster made. I'm a professional mountain bike stunt rider and I need a poster to put on a sandwich board to display my showtimes for people walking by. The top of the poster will say: Mountain Bike (Trials) Stunt Show This text will be centered at the top BUT I want the "(Trials)" to be slightly crooked and a bit opaque with a stamped-looking font and overlap the other words just slightly. Hopefully that makes sense. Somewhere in the middle will be a photoshopped picture of me doing a stunt on my bike. The bottom will have a blank white space titled, "Show Times:" that I can write my showtimes inside of. I've attached a wildly crude and poor drawing of the basic concept. Remember, this is for a stunt show so it must look cool and have some rad colors and design... but also be simple. I will provide a picture of myself riding to be used in the poster. It will take up the middle third.

Target Market(s)

Families, Parents, Kids, general public, mountain bike enthusiastss

Industry/Entity Type

Entertainment Industry

Font styles to use
Sans Serif

Colors

Designer to choose colors to be used in the design.

Requirements
Must have
• A blank, rectangular, white space on the bottom for Show times Labelled "Show Times:"
Nice to have
• I'd like background of the whole poster to be relatively black with cool subtle graphics.

```html
<!DOCTYPE html>
<html lang="en">
<head>
<meta charset="utf-8">
<title>Mountain Bike Trials Stunt Show – Show Times</title>
<link rel="stylesheet" href="https://fonts.googleapis.com/css2?family=Russo+One&family=Josefin+Sans:wght@400;700&display=swap">
<style>
  :root {
    --night: #0e1528;
    --night-deep: #090e1c;
    --sky: #3bb7e6;
    --rule: #d8d8d8;
    --paper: #ffffff;
    --mist-light: #e9eaec;
    --mist-dark: #a9abb0;
    --ink: #111827;
  }
  html, body {
    margin: 0;
    padding: 0;
    width: 800px;
    height: 1200px;
    overflow: hidden;
    background: var(--night);
  }
  .poster {
    position: relative;
    width: 800px;
    height: 1200px;
    overflow: hidden;
    background: radial-gradient(ellipse at 50% 20%, #17203a 0%, var(--night) 55%, var(--night-deep) 100%);
  }
  .poster-art {
    position: absolute;
    inset: 0;
    width: 800px;
    height: 1200px;
  }
  .title-word {
    font-family: "Russo One", sans-serif;
    fill: var(--sky);
  }
  .title-trails {
    font-family: "Josefin Sans", sans-serif;
    font-weight: 700;
    fill: var(--paper);
    opacity: 0.92;
  }
  .showtimes-heading {
    position: absolute;
    left: 58px;
    top: 1002px;
    margin: 0;
    font-family: "Russo One", sans-serif;
    font-weight: 400;
    font-size: 44px;
    line-height: 52px;
    color: var(--paper);
  }
  .showtimes-column {
    position: absolute;
    top: 1030px;
    margin: 0;
    padding: 0;
    list-style: none;
    font-family: "Josefin Sans", sans-serif;
    color: var(--ink);
  }
  .showtimes-column.is-left { left: 254px; }
  .showtimes-column.is-right { left: 442px; top: 1083px; }
  .showtime { height: 53px; }
  .showtime-hour {
    display: block;
    font-weight: 700;
    font-size: 15px;
    line-height: 18px;
  }
  .showtime-venue {
    display: block;
    font-size: 12px;
    line-height: 15px;
    font-variant: small-caps;
    letter-spacing: 0.3px;
  }
  .social-list {
    position: absolute;
    right: 26px;
    top: 1148px;
    margin: 0;
    padding: 0;
    list-style: none;
    display: flex;
    gap: 12px;
    font-family: "Josefin Sans", sans-serif;
    font-weight: 700;
    font-size: 14px;
    color: var(--night);
  }
</style>
</head>
<body>
<main class="poster">
  <svg class="poster-art" viewBox="0 0 800 1200" xmlns="http://www.w3.org/2000/svg">
    <defs>
      <linearGradient id="mistGrad" x1="0" y1="0" x2="1" y2="1">
        <stop offset="0" stop-color="var(--mist-light)"/>
        <stop offset="1" stop-color="var(--mist-dark)"/>
      </linearGradient>
    </defs>

    <polygon class="rider-silhouettes" points="384,24 760,24 760,186 384,102"
             fill="#3bb7e6" opacity="0.14" role="img"
             aria-label="Three blue silhouettes of BMX riders doing jumps"/>

    <polygon class="band-stripe-top" points="0,300 800,442 800,478 0,336" fill="var(--sky)"/>
    <polygon class="rider-photo" points="0,336 800,478 800,1072 0,880" fill="url(#mistGrad)"
             role="img" aria-label="Photo of the stunt rider in a helmet balancing his trials bike, dissolving into dust"/>
    <polygon class="band-stripe-bottom" points="0,880 800,1072 800,1106 0,912" fill="var(--sky)"/>

    <polygon class="times-sheet" points="0,912 800,1106 800,1200 0,1200" fill="var(--paper)"/>
    <polygon class="times-label-panel" points="30,918 232,966 232,1176 30,1120" fill="var(--night)"/>
    <rect class="times-divider" x="402" y="1040" width="4" height="136" fill="var(--sky)"/>

    <line class="title-rule" x1="44" y1="156" x2="240" y2="201" stroke="var(--rule)" stroke-width="6"/>
    <line class="title-rule" x1="580" y1="279" x2="772" y2="323" stroke="var(--rule)" stroke-width="6"/>

    <g transform="translate(408 224) rotate(13)">
      <text class="title-word" x="0" y="0" font-size="140" text-anchor="middle"
            textLength="716" lengthAdjust="spacingAndGlyphs">MOUNTAIN BIKE</text>
    </g>
    <g transform="translate(400 360) rotate(13)">
      <text class="title-word" x="0" y="0" font-size="145" text-anchor="middle"
            textLength="716" lengthAdjust="spacingAndGlyphs">STUNT SHOW</text>
    </g>
    <g transform="translate(414 268) rotate(16)">
      <text class="title-trails" x="0" y="0" font-size="38" text-anchor="middle"
            textLength="270" lengthAdjust="spacing">TRAILS</text>
    </g>
  </svg>

  <h2 class="showtimes-heading">SHOW<br>TIMES:</h2>

  <ul class="showtimes-column is-left">
    <li class="showtime"><span class="showtime-hour">10:00AM</span><span class="showtime-venue">Lorem Ipsum, Dolor</span></li>
    <li class="showtime"><span class="showtime-hour">11:00AM</span><span class="showtime-venue">Lorem Ipsum, Dolor</span></li>
    <li class="showtime"><span class="showtime-hour">12:00PM</span><span class="showtime-venue">Lorem Ipsum, Dolor</span></li>
  </ul>
  <ul class="showtimes-column is-right">
    <li class="showtime"><span class="showtime-hour">11:00AM</span><span class="showtime-venue">Lorem Ipsum, Dolor</span></li>
    <li class="showtime"><span class="showtime-hour">12:00PM</span><span class="showtime-venue">Lorem Ipsum, Dolor</span></li>
  </ul>

  <ul class="social-list">
    <li>Linkly</li>
    <li>Chirpo</li>
    <li>Pixtor</li>
  </ul>
</main>
</body>
</html>
```